Velvet Harbour - R&B Band in Sydney Requires new Business Cards

We're a 6 piece R&B Soul band in Sydney called Velvet Harbour that requires new promotional material including Business Cards.

We are very well known around Sydney and have a resident venue gig at the Marlowe Grand Sydney hotel. We play predominantly old & new school R&B hits.

Our logo is attached, colours are Brown & yellow.
Initial idea was to get sugar packets made up with our logo and contact details.

```html
<!DOCTYPE html>
<html lang="en">
<head>
<meta charset="utf-8">
<title>Velvet Harbour – Business Card</title>
<link href="https://fonts.googleapis.com/css2?family=Anton&display=swap" rel="stylesheet">
<style>
  :root {
    --page: #ffffff;
    --ink: #291a0d;
    --cube: #5e2a05;
    --cube-edge: #2b1a0c;
    --gold: #ffcc00;
  }
  html, body {
    margin: 0;
    width: 1200px;
    height: 1000px;
    overflow: hidden;
    background: var(--page);
  }
  .card {
    display: block;
    width: 1200px;
    height: 1000px;
  }
  .band-name {
    font-family: "Anton", "Impact", sans-serif;
    font-weight: 400;
    fill: var(--ink);
  }
</style>
</head>
<body>
<svg class="card" viewBox="0 0 1200 1000" xmlns="http://www.w3.org/2000/svg">
  <!-- card base -->
  <rect x="69" y="193" width="1062" height="614" fill="var(--cube-edge)"/>

  <!-- cube texture areas -->
  <rect class="texture texture--top" x="69" y="193" width="1062" height="118"
        fill="var(--cube)" role="img" aria-label="Tiled pattern of caramel-coloured cubes"/>
  <rect class="texture texture--bottom" x="69" y="690" width="1062" height="117"
        fill="var(--cube)" role="img" aria-label="Tiled pattern of caramel-coloured cubes"/>

  <!-- horizontal banner with rules -->
  <rect class="banner-rule" x="69" y="302" width="1062" height="12" fill="var(--ink)"/>
  <rect class="banner-rule-line" x="69" y="305" width="1062" height="3" fill="var(--gold)"/>
  <rect class="banner" x="69" y="314" width="1062" height="366" fill="var(--gold)"/>
  <rect class="banner-rule" x="69" y="680" width="1062" height="12" fill="var(--ink)"/>
  <rect class="banner-rule-line" x="69" y="686" width="1062" height="3" fill="var(--gold)"/>

  <!-- name panel -->
  <rect class="panel-outer" x="256" y="282" width="686" height="436" rx="18" fill="var(--gold)"/>
  <rect class="panel-border" x="262" y="288" width="674" height="424" rx="14"
        fill="none" stroke="var(--ink)" stroke-width="4"/>
  <rect class="panel-inner" x="272" y="298" width="654" height="404" rx="10" fill="var(--gold)"/>

  <!-- band name -->
  <text class="band-name" x="282" y="488" font-size="212"
        textLength="636" lengthAdjust="spacingAndGlyphs">VELVET</text>
  <text class="band-name" x="282" y="692" font-size="212"
        textLength="636" lengthAdjust="spacingAndGlyphs">HARBOUR</text>
</svg>
</body>
</html>
```